Webdesign für Sexualpädagogik
Zielgruppe
- Sexualpädagogik, Beratung und Sexualtherapie
- Vorträge und Seminare für Unternehmen / Institutionen Vorträge Sexualität in der Pflege / im Alter / Grenzen wahrnehmen
- Wechseljahreberatung, Beratung in der Lebensmitte
- ZIelgruppe: Menschen, die sich weiternetwickeln möchten, die Problme mit ihrer Sexualität haben, Paare, Jugendliche
letztes Interview in der Zeitung: https://www.talbote-beispiel.ch/talbote/zeitung/frontal-interview/sexualitaet-hoert-nicht-beim-eintritt-ins-spital-auf/
Aufgabenstellung
- bestehende Internetseite siehe unten: Schrift ist Especial Key von Wolkenweg
- auf dem Briefpapier bisher noch der Fachbuchhandel und Onlinhandel, aber beides nicht mehr
- Bilder zum Thema bereist vorhanden
- für Werbeflyer habe ich die Therapie in dunkelblau gehalten udn in der sexualpädagogik in hellblau
der kramhaus wird aus der website entfernet

```html
<!DOCTYPE html>
<html lang="de">
<head>
<meta charset="utf-8">
<title>Wolkenweg – Sexualpädagogik &amp; Beratung</title>
<link rel="stylesheet" href="https://fonts.googleapis.com/css2?family=Handlee&family=Montserrat:wght@400;500&family=Cormorant+Garamond:wght@400;500&display=swap">
<style>
  :root {
    --page-bg: #ffffff;
    --ink: #1d1d1d;
    --ink-soft: #6b6b6b;
    --rule: #d9d9d9;
    --hero-teal-dark: #2f6f80;
    --hero-teal: #5fa3b3;
    --hero-skin: #e9b8a6;
    --hero-skin-light: #f3d6c9;
    --quote-ink: #ffffff;
    --frame-line: rgba(255,255,255,0.75);
  }
  * { box-sizing: border-box; margin: 0; padding: 0; }
  html, body { width: 1200px; height: 800px; overflow: hidden; background: var(--page-bg); }
  .site { width: 1200px; height: 800px; display: flex; flex-direction: column; color: var(--ink); }

  .site-header { position: relative; height: 250px; }
  .practice-tagline {
    position: absolute; left: 40px; top: 130px;
    font-family: "Montserrat", sans-serif; font-size: 12px; line-height: 1.5;
    letter-spacing: 0.04em; color: var(--ink);
  }
  .practice-tagline .secondary { color: var(--ink-soft); font-size: 11px; }
  .social-links {
    position: absolute; right: 40px; top: 22px; display: flex; gap: 14px; list-style: none;
    font-family: "Montserrat", sans-serif; font-size: 11px; color: var(--ink);
  }
  .brand {
    position: absolute; left: 50%; top: 110px; transform: translateX(-50%);
    display: flex; align-items: center; gap: 18px;
    font-family: "Handlee", cursive; font-size: 58px; color: var(--ink);
  }
  .brand-dot { width: 22px; height: 22px; border-radius: 50%; background: var(--ink); }

  .main-nav { height: 50px; border-top: 1px solid var(--rule); border-bottom: 1px solid var(--rule); }
  .main-nav ul {
    list-style: none; display: flex; justify-content: center; gap: 42px; height: 100%; align-items: center;
    font-family: "Montserrat", sans-serif; font-size: 11px; letter-spacing: 0.12em; text-transform: uppercase; color: var(--ink-soft);
  }

  .hero { position: relative; flex: 1; overflow: hidden; }
  .hero-photo {
    position: absolute; inset: 0;
    background:
      radial-gradient(ellipse 420px 300px at 330px 260px, var(--hero-skin-light), var(--hero-skin) 55%, transparent 80%),
      linear-gradient(100deg, #c7d6dc 0%, var(--hero-teal) 45%, var(--hero-teal-dark) 100%);
  }
  .hero-quote {
    position: absolute; left: 640px; top: 60px; width: 440px; height: 360px;
    border: 1px solid var(--frame-line);
    display: flex; flex-direction: column; justify-content: center; align-items: center; text-align: center;
    color: var(--quote-ink); font-family: "Cormorant Garamond", serif;
  }
  .hero-quote blockquote { font-size: 36px; line-height: 1.3; }
  .hero-quote cite { margin-top: 22px; font-style: normal; font-family: "Montserrat", sans-serif; font-size: 11px; letter-spacing: 0.15em; text-transform: uppercase; }
  .slider-arrow { position: absolute; top: 240px; width: 24px; height: 24px; }
  .slider-arrow.prev { left: 30px; }
  .slider-arrow.next { right: 30px; }
</style>
</head>
<body>
<div class="site">
  <header class="site-header">
    <p class="practice-tagline">Sexualpädagogik &amp; Beratung<br><span class="secondary">Therapie · Vorträge · Seminare</span></p>
    <ul class="social-links">
      <li>Plaudernetz</li><li>Kurzpost</li><li>Zwitscherbrett</li><li>Berufsnetz</li>
    </ul>
    <div class="brand"><span class="brand-dot"></span><span>Wolkenweg</span></div>
  </header>

  <nav class="main-nav">
    <ul>
      <li>Home</li><li>Über mich</li><li>Sexualpädagogik</li><li>Beratung</li><li>Therapie</li><li>Vorträge</li><li>Termine</li><li>Blog</li><li>Kontakt</li>
    </ul>
  </nav>

  <section class="hero">
    <div class="hero-photo" role="img" aria-label="Foto: offene Hände halten einen herzförmigen, hellblauen Stein"></div>
    <div class="hero-quote">
      <blockquote>Wenn wir uns<br>selbst nicht lieben,<br>können wir auch<br>keinen anderen<br>Menschen lieben.</blockquote>
      <cite>Lebensweisheit</cite>
    </div>
    <svg class="slider-arrow prev" viewBox="0 0 24 24" aria-hidden="true"><polyline points="15,4 7,12 15,20" fill="none" stroke="#fff" stroke-width="2"/></svg>
    <svg class="slider-arrow next" viewBox="0 0 24 24" aria-hidden="true"><polyline points="9,4 17,12 9,20" fill="none" stroke="#fff" stroke-width="2"/></svg>
  </section>
</div>
</body>
</html>
```